Website Design for Forklift Training Company

DO NOT CONTACT PRIVATELY. ONLY SUBMISSIONS HERE WILL BE CONSIDERED

I need a design for a website that offers forklift training courses.

The company offers accredited, onsite forklift training that are customized for the needs of each individual company. The company offers a variety of courses to operate forklifts and other machinary.

About: "Pembrook Lift Academy Ltd delivers bespoke onsite forklift truck operator training throught the uk.
All our instructors have a wealth of knowledge and expertise to provide your company with all your forklift truck training requirements.
Pembrook Lift Academy Ltd is registered and accredited by qkmvd standards so you can be rest assured that all forklift training is carried out the very highest standard"

I need the following pages designed:
> a) Home Page: Include a header image, ways to contact, about snippet, overview of courses, accreditation that will be received after completing the courses. (See attachments for samples)
> b) About Page
> c) Contact Us Page
> d) Course Page Template: A page that will be used as template for the courses offered. It should contain;
1. Cover image for the course
2. A description of the course
3. A table indicating the various course options
4. Course Objectives
5. What the trainee will receive after doing the course (example: a certification)

Target Market(s)

Industrial Businesses

Number of Pages Required

4 page

Colors
0054AA
0677BA
7BADD7
CADEEF
E8F1F8
0094D4
00A9DD
6FCCEA
C7EBF8
E9F6FB

Requirements
Should not have
• - No Search bar

```html
<!DOCTYPE html>
<html lang="en">
<head>
<meta charset="utf-8">
<title>Pembrook Lift Academy Ltd – Forklift Training</title>
<link href="https://fonts.googleapis.com/css2?family=Poppins:wght@400;500;600;700&display=swap" rel="stylesheet">
<style>
:root{
  --blue-deep:#0054AA;
  --blue:#0677BA;
  --blue-soft:#7BADD7;
  --blue-pale:#CADEEF;
  --blue-mist:#E8F1F8;
  --cyan:#0094D4;
  --cyan-bright:#00A9DD;
  --cyan-soft:#6FCCEA;
  --cyan-pale:#C7EBF8;
  --cyan-mist:#E9F6FB;
  --navy:#0f2747;
  --ink:#1c1c1c;
  --text:#2a2a2a;
  --white:#ffffff;
}
*{box-sizing:border-box;margin:0;padding:0}
html,body{width:1200px;height:2942px;overflow:hidden}
body{position:relative;background:var(--white);font-family:'Poppins',sans-serif;color:var(--text)}
.abs{position:absolute}
a{color:inherit;text-decoration:none}

/* header */
.site-header{left:0;top:0;width:1200px;height:77px;background:var(--white);z-index:5}
.brand{left:88px;top:16px;display:flex;align-items:center;gap:10px}
.brand-square{width:40px;height:40px;background:var(--cyan);border-radius:4px}
.brand-name{font-weight:700;font-size:20px;color:var(--blue);letter-spacing:.2px;line-height:1.1}
.main-nav{left:580px;top:30px;display:flex;gap:34px;font-size:12.5px;font-weight:600;color:#111;letter-spacing:.3px}
.main-nav .active{color:var(--cyan);position:relative}
.main-nav .active::after{content:"";position:absolute;left:0;top:19px;width:18px;height:3px;background:var(--cyan);border-radius:2px}
.btn{display:inline-flex;align-items:center;justify-content:center;border-radius:22px;font-weight:600;font-size:15px}
.btn-fill{background:linear-gradient(90deg,var(--blue),var(--cyan));color:var(--white)}
.btn-line{border:1.5px solid #8a8a8a;color:#111;background:var(--white);font-weight:500}
.inquire{left:967px;top:21px;width:145px;height:35px;background:var(--blue);color:var(--white)}

/* hero */
.hero-photo{left:0;top:77px;width:1200px;height:560px;
  background:linear-gradient(100deg,#3a3228 0%,#5b4f3c 25%,#6a5c3f 45%,#4b4338 65%,#3a3b3e 100%);
  clip-path:polygon(0 0,1200px 0,1200px 313px,485px 551px,0 425px)}
.hero-title{left:90px;top:255px;font-size:46px;font-weight:700;color:var(--white);letter-spacing:.5px}
.hero-cta{left:90px;top:323px;width:150px;height:36px;font-size:15px}
.accred-label{left:709px;top:583px;font-size:17.5px;font-weight:600;color:#111;line-height:21px}
.badge-a{left:893px;top:560px;width:98px;height:60px;background:var(--blue-pale);border-radius:6px}
.badge-b{left:1015px;top:515px;width:97px;height:107px;background:#1f2a78;border:3px solid var(--blue-deep)}

/* about */
.about-title{left:88px;top:716px;font-size:34px;font-weight:700;color:var(--cyan)}
.about-copy{left:88px;top:784px;width:480px;font-size:15px;line-height:20px;color:#222}
.about-copy p{margin-bottom:20px}
.about-more{left:88px;top:1030px;width:143px;height:39px}
.about-photo{left:706px;top:709px;width:406px;height:374px;border-radius:30px;
  background:linear-gradient(120deg,#e6a53a 0%,#c98b3a 25%,#6f8fb0 55%,#e26b2a 100%)}
.about-icon-card{left:649px;top:894px;width:204px;height:165px;background:var(--white);border-radius:26px;box-shadow:0 6px 20px rgba(0,0,0,.12);display:flex;align-items:center;justify-content:center}
.about-icon-fill{width:136px;height:106px;border-radius:10px;background:linear-gradient(90deg,#f2c418,#f2c418 60%,#9a7352)}

/* courses */
.courses-title{left:0;top:1303px;width:1200px;text-align:center;font-size:34px;font-weight:700;color:var(--white)}
.course-card{top:1387px;width:325px;height:355px;background:var(--white);border-radius:3px;overflow:hidden}
.course-head{height:106px;background:var(--cyan-bright);padding:30px 0 0 32px;color:var(--white)}
.course-head h3{font-size:25px;font-weight:600;line-height:28px}
.course-head span{font-size:18px;line-height:22px}
.course-list{list-style:none;padding:42px 20px 0 32px;font-size:14.5px;line-height:20px;color:#222}
.course-list li{position:relative;padding-left:18px;margin-bottom:4px}
.course-list li svg{position:absolute;left:0;top:5px}
.course-more{position:absolute;left:32px;top:292px;width:145px;height:39px}

/* inquiry */
.inquiry-bg{left:0;top:1930px;width:1200px;height:540px;
  background:linear-gradient(180deg,#f4f8fb 0%,#e8eef3 35%,#dfe7e4 65%,#e9eddc 100%)}
.inquiry-card{left:320px;top:2035px;width:737px;height:305px;background:var(--white);box-shadow:0 4px 18px rgba(0,0,0,.06)}
.inquiry-title{position:absolute;left:0;top:34px;width:100%;text-align:center;font-size:25px;font-weight:600;color:var(--cyan)}
.field{position:absolute;height:38px;border:1px solid #e3e3e3;border-radius:20px;display:flex;align-items:center;gap:8px;padding-left:16px;font-size:12.5px;color:#777}
.field-msg{align-items:flex-start;padding-top:10px;border-radius:18px}
.submit{position:absolute;left:314px;top:235px;width:122px;height:37px;font-size:15px}
.forklift-art{left:143px;top:2215px;width:165px;height:165px;border-radius:12px;background:linear-gradient(90deg,#f2c418 0%,#f2c418 70%,#2a2a2a 100%)}
.ground-line{left:305px;top:2351px;width:670px;height:7px;background:#1a1a1a;border-radius:4px}

/* footer */
.footer-brand{left:0;top:2515px;width:1200px;display:flex;justify-content:center;align-items:center;gap:10px}
.footer-brand .brand-square{background:var(--white)}
.footer-brand .brand-name{color:var(--white)}
.footer-h{top:2651px;font-size:18px;font-weight:600;color:var(--cyan-soft)}
.info-item{display:flex;align-items:center;gap:14px}
.info-icon{width:42px;height:42px;border-radius:50%;background:var(--cyan);display:flex;align-items:center;justify-content:center;flex:none}
.info-text{font-size:13.5px;line-height:19px;color:var(--white)}
.info-text .lbl{display:block;color:var(--cyan-soft);font-size:13.5px}
.hours{left:584px;top:2706px;font-size:13.5px;color:var(--white);line-height:32px}
.hours td{padding-right:28px}
.footer-map{left:864px;top:2657px;width:248px;height:143px;background:linear-gradient(135deg,#eef0f2,#e2e6ea);border-radius:4px}
.footer-nav{left:0;top:2860px;width:1200px;display:flex;justify-content:center;gap:48px;font-size:13.5px;color:var(--white)}
.footer-nav .active{color:var(--cyan-soft);text-decoration:underline}
.bottom-bar{left:0;top:2900px;width:1200px;height:42px;background:#0a4a9a}
.copyright{left:88px;top:2911px;font-size:13px;color:var(--white)}
.socials{left:1003px;top:2916px;display:flex;gap:18px}
.socials span{width:12px;height:12px;border-radius:50%;background:var(--white);display:block}
</style>
</head>
<body>

<!-- Header -->
<header class="site-header abs">
  <div class="brand abs"><span class="brand-square"></span><span class="brand-name">PEMBROOK LIFT<br>ACADEMY LTD</span></div>
  <nav class="main-nav abs">
    <a class="active">HOME</a><a>ABOUT US</a><a>COURSE</a><a>CONTACT US</a>
  </nav>
  <a class="btn inquire abs">Inquire Now</a>
</header>

<!-- Hero -->
<div class="hero-photo abs" role="img" aria-label="Forklift instructor in a hard hat and hi-vis vest beside a yellow forklift in a warehouse"></div>
<svg class="abs" style="left:0;top:77px" width="1200" height="570" viewBox="0 0 1200 570">
  <polygon points="70,443 485,551 1200,313 1200,320 1080,360 485,572" fill="#0677BA"/>
  <polygon points="70,443 485,551 1080,353 485,560" fill="#0094D4"/>
</svg>
<h1 class="hero-title abs">FORKLIFT TRAINING</h1>
<a class="btn btn-fill hero-cta abs">Contact Us</a>
<div class="accred-label abs">Forklift Training<br>Accreditation:</div>
<div class="badge-a abs" aria-label="Partner accreditation badge"></div>
<div class="badge-b abs" aria-label="qkmvd accreditation badge"></div>

<!-- About -->
<h2 class="about-title abs">About Us</h2>
<div class="about-copy abs">
  <p>"Pembrook Lift Academy Ltd delivers bespoke onsite forklift truck operator training throughout the UK.</p>
  <p>All our instructors have a wealth of knowledge and expertise to provide your company with all your forklift truck training requirements.</p>
  <p>Pembrook Lift Academy Ltd is registered and accredited by qkmvd standards so you can be rest assured that all forklift training is carried out the very highest standard"</p>
</div>
<a class="btn btn-line about-more abs">Read More</a>
<div class="about-photo abs" role="img" aria-label="Smiling warehouse worker in a blue hard hat and orange safety vest"></div>
<div class="about-icon-card abs"><div class="about-icon-fill" role="img" aria-label="Illustration of a yellow forklift with stacked boxes"></div></div>

<!-- Courses band -->
<svg class="abs" style="left:0;top:1130px" width="1200" height="820" viewBox="0 0 1200 820">
  <defs>
    <linearGradient id="navyFill" x1="0" y1="0" x2="0" y2="1">
      <stop offset="0" stop-color="#12294a"/>
      <stop offset=".6" stop-color="#1b3352"/>
      <stop offset="1" stop-color="#2a3a4a"/>
    </linearGradient>
  </defs>
  <polygon points="0,166 300,18 1200,170 1200,668 900,788 0,670" fill="url(#navyFill)" role="img" aria-label="Dark warehouse scene with a forklift"/>
  <polygon points="0,166 300,10 1200,150 1200,158 300,22 0,172" fill="#0094D4"/>
  <polygon points="0,664 900,782 1200,660 1200,668 900,800 0,672" fill="#0094D4"/>
</svg>
<h2 class="courses-title abs">Forklift Training Courses</h2>

<div class="course-card abs" style="left:88px">
  <div class="course-head"><h3>Forklift Training</h3><span>Courses</span></div>
  <ul class="course-list">
    <li><svg width="10" height="10" viewBox="0 0 10 10"><circle cx="5" cy="5" r="4.3" fill="none" stroke="#0094D4"/><path d="M3 5h4M5.5 3.5 7 5 5.5 6.5" fill="none" stroke="#0094D4"/></svg>Articulated Truck Training Course</li>
    <li><svg width="10" height="10" viewBox="0 0 10 10"><circle cx="5" cy="5" r="4.3" fill="none" stroke="#0094D4"/><path d="M3 5h4M5.5 3.5 7 5 5.5 6.5" fill="none" stroke="#0094D4"/></svg>Multi-Way Lift Training course</li>
    <li><svg width="10" height="10" viewBox="0 0 10 10"><circle cx="5" cy="5" r="4.3" fill="none" stroke="#0094D4"/><path d="M3 5h4M5.5 3.5 7 5 5.5 6.5" fill="none" stroke="#0094D4"/></svg>Counterbalance Training Course</li>
    <li><svg width="10" height="10" viewBox="0 0 10 10"><circle cx="5" cy="5" r="4.3" fill="none" stroke="#0094D4"/><path d="M3 5h4M5.5 3.5 7 5 5.5 6.5" fill="none" stroke="#0094D4"/></svg>Reach Truck Training Course</li>
    <li><svg width="10" height="10" viewBox="0 0 10 10"><circle cx="5" cy="5" r="4.3" fill="none" stroke="#0094D4"/><path d="M3 5h4M5.5 3.5 7 5 5.5 6.5" fill="none" stroke="#0094D4"/></svg>Lorry Crane Training Course</li>
  </ul>
  <a class="btn btn-line course-more">Read More</a>
</div>

<div class="course-card abs" style="left:438px">
  <div class="course-head"><h3>Mewp Training</h3><span>Courses</span></div>
  <ul class="course-list">
    <li><svg width="10" height="10" viewBox="0 0 10 10"><circle cx="5" cy="5" r="4.3" fill="none" stroke="#0094D4"/><path d="M3 5h4M5.5 3.5 7 5 5.5 6.5" fill="none" stroke="#0094D4"/></svg>Cherry Picker Training Course</li>
    <li><svg width="10" height="10" viewBox="0 0 10 10"><circle cx="5" cy="5" r="4.3" fill="none" stroke="#0094D4"/><path d="M3 5h4M5.5 3.5 7 5 5.5 6.5" fill="none" stroke="#0094D4"/></svg>Scissor Lift Training Course</li>
    <li><svg width="10" height="10" viewBox="0 0 10 10"><circle cx="5" cy="5" r="4.3" fill="none" stroke="#0094D4"/><path d="M3 5h4M5.5 3.5 7 5 5.5 6.5" fill="none" stroke="#0094D4"/></svg>Harness And Lanyard Training Course</li>
  </ul>
  <a class="btn btn-line course-more">Read More</a>
</div>

<div class="course-card abs" style="left:787px">
  <div class="course-head"><h3>Other Training</h3><span>Courses</span></div>
  <ul class="course-list">
    <li><svg width="10" height="10" viewBox="0 0 10 10"><circle cx="5" cy="5" r="4.3" fill="none" stroke="#0094D4"/><path d="M3 5h4M5.5 3.5 7 5 5.5 6.5" fill="none" stroke="#0094D4"/></svg>Skid Steer Training Course</li>
    <li><svg width="10" height="10" viewBox="0 0 10 10"><circle cx="5" cy="5" r="4.3" fill="none" stroke="#0094D4"/><path d="M3 5h4M5.5 3.5 7 5 5.5 6.5" fill="none" stroke="#0094D4"/></svg>Front Loading Shovel Training Course</li>
    <li><svg width="10" height="10" viewBox="0 0 10 10"><circle cx="5" cy="5" r="4.3" fill="none" stroke="#0094D4"/><path d="M3 5h4M5.5 3.5 7 5 5.5 6.5" fill="none" stroke="#0094D4"/></svg>Overhead Pendant Crane Training Course</li>
  </ul>
  <a class="btn course-more" style="background:var(--blue);color:var(--white)">Read More</a>
</div>

<!-- Quick inquiry -->
<div class="inquiry-bg abs" role="img" aria-label="Soft illustrated landscape of misty mountains and trees"></div>
<div class="forklift-art abs" role="img" aria-label="Illustration of a yellow forklift"></div>
<div class="ground-line abs"></div>
<form class="inquiry-card abs">
  <h2 class="inquiry-title">Quick Inquiry</h2>
  <div class="field" style="left:32px;top:96px;width:220px">
    <svg width="12" height="12" viewBox="0 0 12 12"><circle cx="6" cy="4" r="2.6" fill="none" stroke="#0677BA"/><path d="M1.5 11.5c0-2.6 2-4 4.5-4s4.5 1.4 4.5 4" fill="none" stroke="#0677BA"/></svg>Name</div>
  <div class="field" style="left:259px;top:96px;width:220px">
    <svg width="10" height="13" viewBox="0 0 10 13"><rect x="1" y="1" width="8" height="11" rx="1.5" fill="none" stroke="#0677BA"/><line x1="4" y1="10" x2="6" y2="10" stroke="#0677BA"/></svg>Phone</div>
  <div class="field" style="left:487px;top:96px;width:220px">
    <svg width="13" height="10" viewBox="0 0 13 10"><rect x=".5" y=".5" width="12" height="9" rx="1" fill="none" stroke="#0677BA"/><path d="M.5 1 6.5 5.5 12.5 1" fill="none" stroke="#0677BA"/></svg>Email</div>
  <div class="field field-msg" style="left:32px;top:150px;width:675px;height:62px">
    <svg width="12" height="12" viewBox="0 0 12 12"><path d="M1 1h10v7l-3 3H1z" fill="none" stroke="#0677BA"/></svg>Message</div>
  <a class="btn btn-fill submit" style="background:var(--blue)">Submit</a>
</form>

<!-- Footer -->
<svg class="abs" style="left:0;top:2410px" width="1200" height="500" viewBox="0 0 1200 500">
  <polygon points="0,120 485,16 1200,120 1200,500 0,500" fill="#0054AA"/>
  <polygon points="110,118 485,8 1090,118 485,26" fill="#0094D4"/>
  <polygon points="0,122 485,30 1200,122 1200,128 485,40 0,128" fill="#0677BA"/>
</svg>
<div class="footer-brand abs"><span class="brand-square"></span><span class="brand-name">PEMBROOK LIFT<br>ACADEMY LTD</span></div>

<h3 class="footer-h abs" style="left:88px">Contatct info</h3>
<div class="info-item abs" style="left:88px;top:2700px">
  <span class="info-icon"><svg width="14" height="18" viewBox="0 0 14 18"><path d="M7 1a6 6 0 0 0-6 6c0 4.5 6 10 6 10s6-5.5 6-10a6 6 0 0 0-6-6z" fill="#fff"/><circle cx="7" cy="7" r="2.2" fill="#0094D4"/></svg></span>
  <span class="info-text">14 Harlow Lane, Brindley,<br>Ashcombe, AB4 2TQ</span>
</div>
<div class="info-item abs" style="left:354px;top:2700px">
  <span class="info-icon"><svg width="16" height="16" viewBox="0 0 16 16"><path d="M3.5 1.5l2.5 3-1.5 1.8c.8 1.8 2.2 3.2 4 4l1.8-1.5 3 2.5-1.5 2.5C7 14.3 1.7 9 1 3z" fill="#fff"/></svg></span>
  <span class="info-text"><span class="lbl">Phone</span>07700 900418</span>
</div>
<div class="info-item abs" style="left:88px;top:2764px">
  <span class="info-icon"><svg width="17" height="13" viewBox="0 0 17 13"><rect x=".5" y=".5" width="16" height="12" rx="1" fill="#fff"/><path d="M1 1.5 8.5 7 16 1.5" fill="none" stroke="#0094D4" stroke-width="1.3"/></svg></span>
  <span class="info-text"><span class="lbl">Email</span>info@pembrook-lift.co.uk</span>
</div>
<div class="info-item abs" style="left:354px;top:2764px">
  <span class="info-icon"><svg width="16" height="15" viewBox="0 0 16 15"><rect x="4" y="1" width="8" height="4" fill="#fff"/><rect x="1" y="5" width="14" height="6" rx="1" fill="#fff"/><rect x="4" y="9" width="8" height="5" fill="#fff" stroke="#0094D4"/></svg></span>
  <span class="info-text"><span class="lbl">Telephone/Fax</span>01632 960274</span>
</div>

<h3 class="footer-h abs" style="left:584px">Business Hours</h3>
<table class="hours abs">
  <tr><td>Mon - Fri</td><td>Open 24 Hours</td></tr>
  <tr><td>Saturday</td><td>6:00 - 18:00</td></tr>
  <tr><td>Sunday</td><td>Appointment Only</td></tr>
</table>
<div class="footer-map abs" role="img" aria-label="Street map showing the office location"></div>

<nav class="footer-nav abs"><a class="active">Home</a><a>About Us</a><a>Course</a><a>Contact Us</a></nav>
<div class="bottom-bar abs"></div>
<p class="copyright abs">Copyright © 2021 Pembrook Lift Academy LTD. All Rights Reserved</p>
<div class="socials abs" aria-label="Social links"><span></span><span></span><span></span><span></span></div>

</body>
</html>
```